PowerPoint template for my training workshop business

I would like to have a PowerPoint template created using my logo and palette materials created by Brivantelox. I train and facilitate workshops using PowerPoint in both corporate and public settings.

I have attached the original design elements to this request.

```html
<!DOCTYPE html>
<html lang="en">
<head>
<meta charset="utf-8">
<title>Marisa Kelden Coaching – Workshop Presentation Template</title>
<link href="https://fonts.googleapis.com/css2?family=Cinzel:wght@500;700&family=Roboto:wght@400;700&display=swap" rel="stylesheet">
<style>
:root{
  --orange:#f7941d;
  --orange-deep:#e8791a;
  --plum:#6b1a4e;
  --plum-dark:#541540;
  --teal:#0d3f47;
  --slate:#8a8ea8;
  --ink:#2b2b2b;
  --paper:#ffffff;
  --sheet:#ffffff;
}
*{box-sizing:border-box;margin:0;padding:0}
html,body{width:771px;height:1200px;overflow:hidden;background:var(--sheet)}
body{position:relative;font-family:"Roboto",Arial,sans-serif;color:var(--ink)}

/* master header: plain business name */
.masthead{position:absolute;top:30px;left:0;width:771px;text-align:center}
.masthead-name{font-family:"Roboto",Arial,sans-serif;font-weight:700;font-size:22px;color:var(--plum);line-height:1}

/* slide grid */
.deck{position:absolute;top:84px;left:13px;display:grid;grid-template-columns:repeat(3,236px);grid-auto-rows:133px;column-gap:19px;row-gap:48px}
.slide{position:relative;overflow:hidden;background:var(--paper);box-shadow:0 5px 12px rgba(0,0,0,.2)}
.photo{position:absolute}

.brand{position:absolute;top:7px;left:15px;font-family:"Roboto",Arial,sans-serif;font-weight:700;font-size:3.6px;color:var(--orange);line-height:1}
.brand.right{left:auto;right:16px}

.foot{position:absolute;left:0;right:0;bottom:5px;height:5px;background:var(--orange);font-size:2.4px;color:#fff;text-align:right;padding-right:22px;line-height:5px}

.title{font-family:"Cinzel",serif;font-weight:700;color:var(--orange);letter-spacing:.05em;line-height:1.15}
.title.light{color:#fff}
.tiny{font-size:2.9px;line-height:1.5;color:#444}
.tiny.light{color:#f2e9ef}
.num{font-family:"Roboto",sans-serif;font-weight:700;color:var(--orange);line-height:1}
.label{font-size:2.6px;font-weight:700;color:var(--ink);text-transform:uppercase;line-height:1.2}
ul.bullets{list-style:disc;padding-left:4px}
ul.bullets li{margin-bottom:1px}
.icon{width:10px;height:10px;stroke:var(--orange);fill:none;stroke-width:1.2}

/* 1 cover */
.cover .photo{inset:0;background:linear-gradient(180deg,#6b1a4e 0%,#8f3e4a 45%,#c2722f 80%,#d48a34 100%)}
.cover-brand{position:absolute;top:30px;left:0;right:0;text-align:center;font-family:"Roboto",Arial,sans-serif;font-weight:700;font-size:8px;color:#fff}
.cover-title{position:absolute;top:60px;left:0;right:0;text-align:center;font-size:8.2px}
.cover-date{position:absolute;right:16px;bottom:8px;font-size:3.6px;color:var(--orange)}

/* 2 about */
.about .photo{left:16px;top:20px;width:76px;height:76px;border-radius:50%;background:radial-gradient(circle,#d9d6d2,#8c8781);border:3px solid var(--orange)}
.about .caption{position:absolute;left:16px;width:76px;top:101px;text-align:center;font-size:3.2px}
.about .caption b{display:block;font-family:"Cinzel",serif;font-size:4px}
.about .title{position:absolute;left:124px;top:25px;font-size:7px}
.about .body{position:absolute;left:124px;top:37px;width:96px}

/* 3 toc */
.toc .photo{left:0;top:0;width:118px;height:133px;background:linear-gradient(180deg,#e9874a 0%,#d8703b 55%,#3a2520 80%,#1e1613 100%)}
.toc .title{position:absolute;left:16px;top:12px;font-size:6.2px;color:#fff}
.toc-grid{position:absolute;left:126px;top:8px;width:104px;display:grid;grid-template-columns:1fr 1fr;row-gap:7px;text-align:center}
.toc-grid .num{font-size:10px}
.toc-grid .tiny{font-size:1.8px;color:#666}

/* 4 principles */
.principles .title{position:absolute;left:0;right:0;top:17px;text-align:center;font-size:6.8px}
.principles .photo{left:0;top:32px;width:236px;height:63px;background:linear-gradient(90deg,#d3852f,#b5643d,#93484a)}
.pillars{position:absolute;left:20px;top:45px;width:200px;display:grid;grid-template-columns:repeat(4,1fr);text-align:center;color:#fff}
.pillars div{border-right:.5px solid rgba(255,255,255,.5);padding:0 4px}
.pillars div:last-child{border:0}
.pillars .icon{stroke:#fff;width:11px;height:11px}
.pillars h4{font-family:"Cinzel",serif;font-size:3.6px;margin:2px 0}
.pillars p{font-size:2.6px;line-height:1.5}
.principles .note{position:absolute;left:28px;top:104px;width:180px;text-align:center}

/* 5 about workshop */
.workshop{background:var(--plum)}
.workshop .photo{left:0;top:8px;width:100px;height:125px;background:linear-gradient(135deg,#3f6b2c,#a7b87a 55%,#4d6e34);clip-path:polygon(4% 2%,96% 0,100% 40%,94% 100%,0 98%,3% 55%)}
.workshop .title{position:absolute;left:125px;top:20px;font-size:7px}
.workshop .body{position:absolute;left:125px;top:33px;width:96px}
.workshop .body b{display:block;font-size:2.9px;color:#fff;margin:3px 0 1px 13px}
.workshop .indent{padding-left:13px}

/* 6 theory */
.theory{background:var(--teal)}
.theory .title{position:absolute;left:15px;top:25px;font-size:7px}
.theory .body{position:absolute;left:20px;top:50px;width:105px}
.theory .photo{right:0;top:6px;width:110px;height:125px;background:linear-gradient(160deg,#6f4a2f,#c8b9a4 50%,#5a3c27);clip-path:polygon(8% 3%,100% 0,100% 100%,10% 97%,0 50%)}

/* 7 picture */
.picture .photo{inset:0;background:linear-gradient(160deg,#7a2a1e,#e0541e 35%,#c23a26 60%,#6b1a4e)}
.picture .title{position:absolute;left:16px;top:93px;font-size:10.5px;color:#fff}

/* 8 steps */
.steps .photo{left:0;top:0;width:236px;height:57px;background:linear-gradient(90deg,#8c1e3c,#b63342 50%,#6b1a4e)}
.steps .title{position:absolute;left:17px;top:20px;font-size:7px;color:#fff}
.steps-row{position:absolute;left:20px;top:71px;width:196px;display:grid;grid-template-columns:repeat(3,1fr);text-align:center}
.steps-row .num{font-size:11px;margin-bottom:2px}
.steps-row .tiny{font-size:1.9px;color:#666}

/* 9 topic */
.topic .title{position:absolute;left:21px;top:30px;font-size:8px}
.topic .body{position:absolute;left:21px;top:52px;width:96px}
.topic .photo{left:118px;top:0;width:118px;height:133px;background:linear-gradient(180deg,#dfe7ec 0%,#6d8476 35%,#3f5a41 65%,#3e4d52 100%)}

/* 10 expectations */
.expect .title{position:absolute;left:0;right:0;top:17px;text-align:center;font-size:6.5px}
.expect-grid{position:absolute;left:26px;top:35px;width:190px;display:grid;grid-template-columns:repeat(3,1fr);row-gap:10px;column-gap:8px}
.expect-grid h4{font-family:"Cinzel",serif;font-size:3.3px;color:var(--orange);margin:2px 0 1px}
.expect-grid .tiny{font-size:2.5px}

/* 11 achieve */
.achieve .photo{left:0;top:0;width:236px;height:57px;background:linear-gradient(100deg,#8b2747,#b8606a 50%,#4a1236)}
.achieve .title{position:absolute;left:17px;top:20px;font-size:7px;color:#fff}
.achieve-grid{position:absolute;left:19px;top:67px;width:200px;display:grid;grid-template-columns:1fr 1fr;row-gap:9px;column-gap:8px}
.achieve-grid > div{display:flex;gap:5px}
.achieve-grid h4{font-family:"Cinzel",serif;font-size:3.3px;color:var(--orange);margin-bottom:1px}
.achieve-grid .tiny{font-size:2.5px}

/* 12 warm up */
.warm{background:var(--teal)}
.warm .photo{left:10px;top:6px;width:226px;height:58px;background:linear-gradient(90deg,#3e6b34,#c9433f 35%,#3d8ec4 65%,#4e7a3c);clip-path:polygon(0 60%,25% 30%,60% 8%,100% 0,100% 55%,70% 75%,30% 95%,5% 100%)}
.warm .title{position:absolute;left:29px;top:58px;font-size:8.5px}
.warm .body{position:absolute;left:31px;top:84px;width:150px}

/* 13 section */
.section .photo{inset:0;background:linear-gradient(180deg,#6f3e56,#a94a5e 40%,#c8455a 70%,#b43f4f)}
.section .rule{position:absolute;left:74px;width:90px;height:.5px;background:var(--orange)}
.section .title{position:absolute;left:0;right:0;top:50px;text-align:center;font-size:7.2px}

/* 14 exercise */
.exercise .title{position:absolute;left:0;right:0;top:17px;text-align:center;font-size:6.5px}
.ex-grid{position:absolute;left:15px;top:30px;width:206px;height:103px;display:grid;grid-template-columns:repeat(4,1fr);grid-template-rows:1fr 1fr}
.ex-grid .cell{position:relative;padding:8px 4px 0}
.ex-grid .num{font-size:10px;text-align:center;margin-bottom:3px}
.ex-grid ul{font-size:1.9px;color:#555}
.ph-a{background:linear-gradient(180deg,#cfe0e6,#4d7e73 55%,#6d5a45)}
.ph-b{background:linear-gradient(135deg,#2f5a2b,#c9c1b5 50%,#3f6a33)}
.ph-c{background:linear-gradient(135deg,#5a3c27,#cbbba6 50%,#6d4a30)}
.ph-d{background:linear-gradient(135deg,#d8d6d2,#7b7671 60%,#c7c4bf)}

/* 15 numbered photos */
.mosaic{display:grid;grid-template-columns:repeat(3,1fr);grid-template-rows:1fr 1fr}
.mosaic .cell{position:relative;padding:14px 10px 0}
.mosaic .num{font-size:17px;margin-bottom:3px}
.mosaic .label{font-size:2.3px}
.mosaic .page{position:absolute;right:10px;bottom:6px;font-size:2.3px;color:#666}

/* 16 two column */
.twocol .title{position:absolute;left:20px;top:30px;font-size:8.2px;color:var(--ink)}
.twocol .col-a{position:absolute;left:20px;top:63px;width:93px}
.twocol .col-b{position:absolute;left:122px;top:23px;width:95px}
.twocol p{margin-bottom:3px}

/* 17 image placeholder */
.images{background:var(--plum)}
.images .photo.top{left:0;top:0;width:140px;height:67px;background:linear-gradient(180deg,#d9e4ea,#6f8d7b 45%,#4a4a3c)}
.images .photo.bottom{left:98px;top:67px;width:138px;height:66px;background:linear-gradient(180deg,#cfd9dd,#5d7760 50%,#3b4c4f)}
.images .t1{position:absolute;right:14px;top:20px;text-align:right;font-size:7px}
.images .b1{position:absolute;left:145px;top:40px;width:80px}
.images .t2{position:absolute;left:17px;top:79px;font-size:7px}
.images .b2{position:absolute;left:17px;top:97px;width:78px}

/* 18 triangle */
.triangle .title{position:absolute;left:0;right:0;top:17px;text-align:center;font-size:6.5px}
.triangle svg.tri{position:absolute;left:25px;top:38px;width:72px;height:72px}
.tri-list{position:absolute;left:117px;top:29px;width:100px}
.tri-list div{display:flex;gap:6px;align-items:center;margin-bottom:6px}
.tri-list .num{font-size:10px;width:14px}
.tri-list .num.teal{color:var(--teal)}
.tri-list .num.plum{color:var(--plum)}
.tri-list .num.slate{color:var(--slate)}
.tri-list .label{font-size:2.3px;margin-bottom:1px}
.tri-list .tiny{font-size:2.3px}
</style>
</head>
<body>

<header class="masthead">
  <div class="masthead-name">Marisa Kelden Coaching</div>
</header>

<main class="deck">

  <!-- cover -->
  <section class="slide cover">
    <div class="photo" role="img" aria-label="Lake at dusk between mountains, a person sitting at the end of a wooden pier"></div>
    <div class="cover-brand">Marisa Kelden Coaching</div>
    <h1 class="title cover-title">WORKSHOP<br>EMBRACING BODY, MIND &amp; SPIRIT</h1>
    <div class="cover-date">Date: may 5, 2020</div>
  </section>

  <!-- about -->
  <section class="slide about">
    <div class="brand">Marisa Kelden Coaching</div>
    <div class="photo" role="img" aria-label="Coach working at a laptop beside a bright window"></div>
    <div class="caption">CEO / Manager<b>MARISA KELDEN</b></div>
    <h2 class="title">ABOUT MARISA</h2>
    <div class="body tiny">
      <p>Marisa has guided teams and public groups for many years. Her sessions blend movement, reflection and clear practical tools so each person leaves with steps they can use straight away at work and at home. She works with leaders, new managers and open community groups, and keeps every room calm, warm and focused on real change.</p>
      <p style="margin-top:3px">Before coaching she led people in busy service teams, which shapes her plain, friendly style. She believes that lasting growth starts with the body, settles in the mind and is carried forward by spirit and steady daily habits.</p>
    </div>
    <div class="foot">Page 2</div>
  </section>

  <!-- table of contents -->
  <section class="slide toc">
    <div class="photo" role="img" aria-label="Silhouette of a woman against an orange sunset city skyline"></div>
    <h2 class="title">TABLE OF CONTENTS</h2>
    <div class="toc-grid">
      <div><div class="num">01</div><div class="label">Welcome<br>and intent</div><p class="tiny">Why we gather and what we hope to gain</p></div>
      <div><div class="num">02</div><div class="label">Our<br>principles</div><p class="tiny">How we agree to work as a group today</p></div>
      <div><div class="num">03</div><div class="label">Theory<br>overview</div><p class="tiny">The main ideas behind the session plan</p></div>
      <div><div class="num">04</div><div class="label">Warm up<br>activity</div><p class="tiny">A short movement to open the body</p></div>
      <div><div class="num">05</div><div class="label">Guided<br>exercises</div><p class="tiny">Practice in pairs and small groups</p></div>
      <div><div class="num">06</div><div class="label">Reflection<br>and close</div><p class="tiny">What we take home after the day ends</p></div>
    </div>
    <div class="foot" style="background:none;color:#666;bottom:3px">Page 4</div>
  </section>

  <!-- guiding principles -->
  <section class="slide principles">
    <div class="brand">Marisa Kelden Coaching</div>
    <h2 class="title">GUIDING PRINCIPLES</h2>
    <div class="photo" role="img" aria-label="Warm-toned mountain lake scene behind the principles"></div>
    <div class="pillars">
      <div><svg class="icon" viewBox="0 0 12 12"><circle cx="6" cy="6" r="4.5"/><circle cx="6" cy="6" r="1.8"/></svg><h4>SINGLY</h4><p>Each person has his or her own unique lived experience.</p></div>
      <div><svg class="icon" viewBox="0 0 12 12"><path d="M2 10h8M3 10V5l3-3 3 3v5"/></svg><h4>RESPECT</h4><p>Each of us will respect each other's opinions and feelings.</p></div>
      <div><svg class="icon" viewBox="0 0 12 12"><circle cx="6" cy="6.5" r="4.3"/><path d="M6 4v2.7l1.8 1M4.5 1h3"/></svg><h4>PUNTUAL</h4><p>Each of us will try to be punctual.</p></div>
      <div><svg class="icon" viewBox="0 0 12 12"><path d="M3 10V5a3 3 0 0 1 6 0v1l1 2H8v2z"/></svg><h4>OPEN MIND</h4><p>Each of us will keep an open mind about new ideas and learn from each other's experiences.</p></div>
    </div>
    <p class="note tiny">These four principles frame every session we share, so the room stays safe, kind and focused while each person takes part at a pace that suits them best.</p>
    <div class="foot">Page 3</div>
  </section>

  <!-- about workshop -->
  <section class="slide workshop">
    <div class="brand right">Marisa Kelden Coaching</div>
    <div class="photo" role="img" aria-label="Woman with short hair looking up among green leaves"></div>
    <h2 class="title">ABOUT WORKSHOP</h2>
    <div class="body tiny light">
      <p>This workshop brings body, mind and spirit together through simple practice, honest talk and time to reflect. It suits teams and open groups who want calm focus and fresh energy.</p>
      <b>Lorem ipsum</b><p class="indent">Gentle movement opens the day and helps the group settle in.</p>
      <b>Lorem ipsum</b><p class="indent">Guided talks share the core ideas in plain everyday language.</p>
      <b>Lorem ipsum</b><p class="indent">Quiet reflection closes each part so learning can take root.</p>
    </div>
  </section>

  <!-- theory -->
  <section class="slide theory">
    <div class="brand">Marisa Kelden Coaching</div>
    <h2 class="title">THEORY ABOUT<br>OUR WORKSHOP</h2>
    <ul class="body bullets tiny light">
      <li>The body holds stress long before we notice it, so we begin with breath and posture to bring attention back into the room.</li>
      <li>A calm body makes space for a clear mind and better choices.</li>
      <li>Small habits repeated daily shape lasting change more than one large effort, so each tool is short and easy to repeat.</li>
      <li>Shared stories build trust and help ideas stick.</li>
      <li>Spirit here means purpose: knowing what matters and acting on it with care.</li>
      <li>Rest is part of growth, not a break from it.</li>
    </ul>
    <div class="photo" role="img" aria-label="Desk from above with coffee cup, photos and a hand writing in a notebook"></div>
  </section>

  <!-- picture -->
  <section class="slide picture">
    <div class="photo" role="img" aria-label="Glowing orange neon sign with a handwritten word about change"></div>
    <div class="brand right">Marisa Kelden Coaching</div>
    <h2 class="title light">PICTURE TO<br>DESCRIBE THE TOPIC</h2>
  </section>

  <!-- steps -->
  <section class="slide steps">
    <div class="photo" role="img" aria-label="Red neon sign about change seen up close"></div>
    <div class="brand right">Marisa Kelden Coaching</div>
    <h2 class="title">STEPS TO ACHIEVE<br>OUR GOALS</h2>
    <div class="steps-row">
      <div><div class="num">01</div><div class="label">Notice<br>the pattern</div><p class="tiny">See the habit you want to shift today</p></div>
      <div><div class="num">02</div><div class="label">Choose<br>one action</div><p class="tiny">Pick a small step you can repeat daily</p></div>
      <div><div class="num">03</div><div class="label">Review<br>and adjust</div><p class="tiny">Check in weekly and tune the next step</p></div>
    </div>
    <div class="foot">Page 8</div>
  </section>

  <!-- topic -->
  <section class="slide topic">
    <div class="brand">Marisa Kelden Coaching</div>
    <h2 class="title">WHAT'S TOPIC<br>ABOUT</h2>
    <ul class="body bullets tiny">
      <li>Today we look at how stress shows up in the body and how simple daily practice can bring calm, focus and steady energy back into work and home life.</li>
      <li>We explore the link between posture, breath and mood, and practise tools that take less than five minutes each.</li>
      <li>Each idea is tested in the room so you leave with what works for you.</li>
    </ul>
    <div class="photo" role="img" aria-label="Mountain valley with a still green lake"></div>
  </section>

  <!-- expectations -->
  <section class="slide expect">
    <div class="brand">Marisa Kelden Coaching</div>
    <h2 class="title">DESCRIBE EXPECTATIONS</h2>
    <div class="expect-grid">
      <div><svg class="icon" viewBox="0 0 12 12"><rect x="1.5" y="3" width="4" height="7"/><rect x="6.5" y="3" width="4" height="7"/></svg><h4>CHECK</h4><p class="tiny">Take a moment to check how you feel as the day begins.</p></div>
      <div><svg class="icon" viewBox="0 0 12 12"><path d="M1 10h10M3 10l3-7 3 7M4.3 7h3.4"/></svg><h4>STUDY</h4><p class="tiny">Study each idea and ask how it fits your own daily life.</p></div>
      <div><svg class="icon" viewBox="0 0 12 12"><circle cx="6" cy="6" r="4.5"/><path d="M4 6.5l1.5 1.5L8.5 4.5"/></svg><h4>ANALYZE</h4><p class="tiny">Look at what helps and what holds you back from change.</p></div>
      <div><svg class="icon" viewBox="0 0 12 12"><rect x="1.5" y="1.5" width="9" height="6"/><path d="M3 10.5h6M6 7.5v3"/></svg><h4>INVESTIGATE</h4><p class="tiny">Explore new habits with curiosity and without any judgement.</p></div>
      <div><svg class="icon" viewBox="0 0 12 12"><circle cx="3" cy="3" r="1.5"/><circle cx="9" cy="3" r="1.5"/><path d="M3 5v5M9 5v5M3 7h6"/></svg><h4>SHARE</h4><p class="tiny">Share what you notice so the whole group can learn too.</p></div>
      <div><svg class="icon" viewBox="0 0 12 12"><path d="M1 6l3-3 2 2 2-2 3 3-5 4z"/></svg><h4>DEAL</h4><p class="tiny">Agree on one step you will keep after the session ends.</p></div>
    </div>
    <div class="foot">Page 10</div>
  </section>

  <!-- achieve -->
  <section class="slide achieve">
    <div class="photo" role="img" aria-label="Hands writing in a notebook with photos on a desk"></div>
    <div class="brand right">Marisa Kelden Coaching</div>
    <h2 class="title">WHAT WE WANT<br>TO ACHIEVE?</h2>
    <div class="achieve-grid">
      <div><svg class="icon" viewBox="0 0 12 12"><rect x="1.5" y="2" width="9" height="6"/><path d="M4 10h4M6 8v2"/></svg><div><h4>KNOWLEDGE</h4><p class="tiny">Clear ideas on how body and mind work together each day.</p></div></div>
      <div><svg class="icon" viewBox="0 0 12 12"><circle cx="6" cy="3.5" r="2"/><path d="M2 10.5a4 4 0 0 1 8 0"/></svg><div><h4>RECOGNITION</h4><p class="tiny">Notice the signs of stress early and respond with care.</p></div></div>
      <div><svg class="icon" viewBox="0 0 12 12"><path d="M3 11V6l1-4 2 2 2-2 1 4v5z"/></svg><div><h4>EMPOWER</h4><p class="tiny">Feel able to choose small steps that make real change.</p></div></div>
      <div><svg class="icon" viewBox="0 0 12 12"><circle cx="6" cy="5" r="4"/><path d="M6 9v2.5M4 5h4M6 3v4"/></svg><div><h4>BRAIN DEVELOP</h4><p class="tiny">Build focus and calm through short, steady daily practice.</p></div></div>
    </div>
    <div class="foot">Page 11</div>
  </section>

  <!-- warm up -->
  <section class="slide warm">
    <div class="brand">Marisa Kelden Coaching</div>
    <div class="photo" role="img" aria-label="Team of players in red and blue bibs running on a green field"></div>
    <h2 class="title">WARM UP<br>ACTIVITY</h2>
    <ul class="body bullets tiny light">
      <li>Stand in a circle and take three slow breaths together as a group;<br>roll the shoulders and loosen the neck.</li>
      <li>Walk the room at an easy pace and greet each person you pass;<br>then speed up a little and slow down again.</li>
      <li>Pair up and share one word that sums up how you feel right now;<br>swap partners and repeat twice.</li>
    </ul>
  </section>

  <!-- section divider -->
  <section class="slide section">
    <div class="photo" role="img" aria-label="Lake between mountains with a wooden pier in rose tones"></div>
    <div class="rule" style="top:44px"></div>
    <h2 class="title">SECTION 1<br>EXERCISE<br>EMBRACING BODY,<br>MIND &amp; SPIRIT</h2>
    <div class="rule" style="top:93px"></div>
  </section>

  <!-- exercise -->
  <section class="slide exercise">
    <div class="brand">Marisa Kelden Coaching</div>
    <h2 class="title">EXERCISE # 1</h2>
    <div class="ex-grid">
      <div class="cell"><div class="num">01</div><ul class="bullets"><li>Stand tall and breathe slowly</li><li>Notice your feet on the floor</li><li>Relax your jaw and shoulders</li><li>Hold for one full minute</li></ul></div>
      <div class="cell ph-a" role="img" aria-label="Person sitting on a pier by a mountain lake"></div>
      <div class="cell"><div class="num">03</div><ul class="bullets"><li>Write one thing you value</li><li>Share it with a partner</li><li>Listen without advice</li><li>Swap roles and repeat</li></ul></div>
      <div class="cell ph-b" role="img" aria-label="Woman looking up among green leaves"></div>
      <div class="cell ph-c" role="img" aria-label="Desk with coffee and a notebook"></div>
      <div class="cell"><div class="num">02</div><ul class="bullets"><li>Close your eyes gently</li><li>Count ten slow breaths</li><li>Notice where tension sits</li><li>Let it soften on each out</li></ul></div>
      <div class="cell ph-d" role="img" aria-label="Person working at a laptop by a window"></div>
      <div class="cell"><div class="num">04</div><ul class="bullets"><li>Pick one small daily step</li><li>Say it out loud to the group</li><li>Set a time to do it</li><li>Check in next week</li></ul></div>
    </div>
    <div class="foot" style="background:none;color:#666;bottom:3px">Page 14</div>
  </section>

  <!-- numbered photo grid -->
  <section class="slide mosaic">
    <div class="cell ph-d" role="img" aria-label="Person working at a laptop by a bright window"></div>
    <div class="cell"><div class="num">02</div><div class="label">We build calm habits<br>one day at a time<br>we grow together<br>we keep it simple</div></div>
    <div class="cell ph-b" role="img" aria-label="Woman looking up among green leaves"></div>
    <div class="cell"><div class="num">01</div><div class="label">We start with the body<br>then settle the mind<br>then act with purpose<br>we share what we learn</div></div>
    <div class="cell ph-c" role="img" aria-label="Desk with coffee cup and a hand writing in a notebook"></div>
    <div class="cell"><div class="num">03</div><div class="label">We take home one step<br>we practise it daily<br>we review each week<br>we keep going</div><div class="page">Page 15</div></div>
  </section>

  <!-- two column -->
  <section class="slide twocol">
    <div class="brand">Marisa Kelden Coaching</div>
    <h2 class="title">TWO COLUMN<br>TEXT LAYOUTS</h2>
    <div class="col-a tiny">
      <p>Use this layout to share a short story or case from past sessions. Keep each paragraph brief so the group can read it quickly and stay with you as you speak.</p>
      <p>A second paragraph can hold a question for the room, an example from daily life or a simple tip that people can try during the next break.</p>
    </div>
    <div class="col-b tiny">
      <p>The right column suits longer notes, such as the steps of an exercise or the thinking behind it. Break the text into short blocks and give each one a clear point so nothing feels heavy on screen. Keep a calm pace and pause between ideas.</p>
      <p>When the topic is rich, split it across two slides rather than shrinking the type. People remember more when each slide carries one idea, a clear picture and a little space to breathe around the words that matter most today.</p>
    </div>
    <div class="foot">Page 17</div>
  </section>

  <!-- image placeholder -->
  <section class="slide images">
    <div class="photo top" role="img" aria-label="Person sitting at the end of a pier on a mountain lake"></div>
    <div class="photo bottom" role="img" aria-label="Misty mountain valley above a calm lake"></div>
    <div class="brand right">Marisa Kelden Coaching</div>
    <h2 class="title t1">IMAGE<br>PLACEHOLDER</h2>
    <ul class="b1 bullets tiny light">
      <li>Place a calm photo here to set the tone for the next part of the day.</li>
      <li>Choose images with space, light and nature to support reflection.</li>
    </ul>
    <h2 class="title t2">IMAGE<br>BACKGROUNDS</h2>
    <ul class="b2 bullets tiny light">
      <li>Use a wide scene behind the text to frame a key message.</li>
      <li>Keep the words short so they stay easy to read on the image.</li>
    </ul>
  </section>

  <!-- triangle infographic -->
  <section class="slide triangle">
    <div class="brand">Marisa Kelden Coaching</div>
    <h2 class="title">TRIANGLE INFOGRAPHIC</h2>
    <svg class="tri" viewBox="0 0 100 100" aria-hidden="true">
      <polygon points="50,0 75,50 25,50" fill="var(--orange)"/>
      <polygon points="25,50 50,100 0,100" fill="var(--teal)"/>
      <polygon points="25,50 75,50 50,100" fill="var(--plum)"/>
      <polygon points="75,50 100,100 50,100" fill="var(--slate)"/>
    </svg>
    <div class="tri-list">
      <div><span class="num">01</span><span><div class="label">Be the best version</div><p class="tiny">Start from strength and build on what already works well for you.</p></span></div>
      <div><span class="num teal">02</span><span><div class="label">Offer steady support</div><p class="tiny">Lean on the group and give back the same care you receive today.</p></span></div>
      <div><span class="num plum">03</span><span><div class="label">Release old patterns</div><p class="tiny">Let go of habits that drain energy and make room for new ones.</p></span></div>
      <div><span class="num slate">04</span><span><div class="label">Offer 24/7 support</div><p class="tiny">Keep the tools close so help is there whenever you need it most.</p></span></div>
    </div>
    <div class="foot">Page 18</div>
  </section>

</main>
</body>
</html>
```